Business Card Design - Local Discount Club

Looking for a fun business card for a local discount club. One side should be the logo only and the other should be have :

Name
Title
Phone, Email
Website

```html
<!DOCTYPE html>
<html lang="en">
<head>
<meta charset="utf-8">
<title>The Harbor Pass — Business Card</title>
<link href="https://fonts.googleapis.com/css2?family=Montserrat:wght@400;500;600;700&display=swap" rel="stylesheet">
<style>
  :root {
    --backdrop: #3b3b3d;
    --card-white: #ffffff;
    --club-blue: #3757b8;
    --sky-blue: #2fa3ea;
    --aqua: #4fe0f7;
    --lime: #9dfc8a;
    --text-white: #ffffff;
  }
  * { margin: 0; padding: 0; box-sizing: border-box; }
  html, body {
    width: 1200px; height: 1200px; overflow: hidden;
    background: var(--backdrop);
    font-family: "Montserrat", sans-serif;
  }
  .canvas {
    position: relative; width: 1200px; height: 1200px;
  }
  .card {
    position: absolute; left: 250px; width: 700px; height: 400px;
    border-radius: 30px; overflow: hidden; background: var(--card-white);
    box-shadow: 0 18px 40px rgba(0,0,0,.45);
  }
  .card--front { top: 130px; }
  .card--back { top: 660px; }
  .front-waves { position: absolute; inset: 0; }
  .brand {
    position: absolute; display: flex; align-items: center; gap: 12px;
    color: var(--club-blue); font-weight: 700; letter-spacing: .02em;
    white-space: nowrap;
  }
  .brand__dot { border-radius: 50%; background: var(--aqua); flex: none; }
  .card--front .brand { left: 50%; top: 95px; transform: translateX(-50%); font-size: 34px; }
  .card--front .brand__dot { width: 18px; height: 18px; }
  .card--back .brand { left: 50%; top: 50%; transform: translate(-50%, -60%); font-size: 52px; }
  .card--back .brand__dot { width: 26px; height: 26px; }
  .holder {
    position: absolute; left: 48px; bottom: 48px;
    padding-left: 18px; border-left: 5px solid var(--aqua);
  }
  .holder__name { color: var(--aqua); font-weight: 600; font-size: 34px; line-height: 1.05; }
  .holder__title { color: var(--text-white); font-weight: 500; font-size: 15px; letter-spacing: .06em; margin-top: 4px; }
  .contacts {
    position: absolute; right: 48px; top: 230px; list-style: none;
    color: var(--text-white); font-size: 16px; font-weight: 500;
  }
  .contacts li { display: flex; align-items: center; gap: 10px; margin-bottom: 9px; }
  .contacts svg { width: 18px; height: 18px; flex: none; }
  .stripe { position: absolute; left: 0; right: 0; bottom: 0; height: 22px; display: flex; }
  .stripe span { flex: 1; }
  .stripe__blue { background: var(--club-blue); }
  .stripe__aqua { background: var(--aqua); }
  .stripe__lime { background: var(--lime); }
</style>
</head>
<body>
<main class="canvas">

  <section class="card card--front">
    <svg class="front-waves" viewBox="0 0 700 400" preserveAspectRatio="none" aria-hidden="true">
      <path d="M0,268 Q430,262 700,62 L700,400 L0,400 Z" fill="var(--club-blue)"/>
      <path d="M70,262 Q430,254 700,30 L700,52 Q425,262 70,266 Z" fill="var(--sky-blue)"/>
    </svg>

    <div class="brand"><span class="brand__dot"></span>THE HARBOR PASS</div>

    <div class="holder">
      <p class="holder__name">JOHN DOE</p>
      <p class="holder__title">POSITION</p>
    </div>

    <ul class="contacts">
      <li>
        <svg viewBox="0 0 24 24"><path fill="var(--aqua)" d="M6.6 10.8a15.1 15.1 0 0 0 6.6 6.6l2.2-2.2a1 1 0 0 1 1-.25 11.4 11.4 0 0 0 3.6.57 1 1 0 0 1 1 1V20a1 1 0 0 1-1 1A17 17 0 0 1 3 4a1 1 0 0 1 1-1h3.5a1 1 0 0 1 1 1c0 1.25.2 2.45.57 3.57a1 1 0 0 1-.25 1z"/></svg>
        (000) 000 0000
      </li>
      <li>
        <svg viewBox="0 0 24 24"><rect x="2" y="5" width="20" height="14" rx="1.5" fill="var(--aqua)"/><path d="M3 6l9 7 9-7" fill="none" stroke="var(--club-blue)" stroke-width="1.8"/></svg>
        email@youremail.com
      </li>
      <li>
        <svg viewBox="0 0 24 24" fill="none" stroke="var(--aqua)" stroke-width="1.8"><circle cx="12" cy="12" r="9.5"/><ellipse cx="12" cy="12" rx="4" ry="9.5"/><path d="M2.5 12h19M4 7h16M4 17h16"/></svg>
        www.yourwebsite.com
      </li>
    </ul>
  </section>

  <section class="card card--back">
    <div class="brand"><span class="brand__dot"></span>THE HARBOR PASS</div>
    <div class="stripe">
      <span class="stripe__blue"></span>
      <span class="stripe__aqua"></span>
      <span class="stripe__lime"></span>
    </div>
  </section>

</main>
</body>
</html>
```